Dalton & Vesh Periodontics and Implant Solutions Business Card

We are a specialty dental practice- implants and periodontal surgery. We have just re-designed our logo and are building a new office and would like to re-design our business card. We are looking for something professional with a creative and artsy twist- something to stand out among the rest! Happy Designing!

I have uploaded all versions of our new logo and our current business card. We have 3 locations and 2 doctors.
Updates

Target Market(s)

55+

Industry/Entity Type

Dental

Contact Information for Business Card

Needs Names, logo, locations- professional and artsy!

Colors
0555a3
0592cd
34a7d7
3277b5
85cae6
85acd3
cee9f5
ecf7fb

Requirements
Must have
• our names:
• Gavin T. Dalton D.M.D.
• Marla P. Vesh D.M.D.
• Diplomate of the National Council of Gum Surgery
• Address locations:
• 462 N. Larkspur Avenue Suite 210B Plantation, FL 33324
• Tel: 954-603-2281 Fax: 954-603-2895
• 5174 Hollins Lane #C-3 Boca Raton, FL 33434
• Tel: 561-327-6018 Fax: 561-327-6092
• 381 Northwest 7th Street #412 Miami FL 33131
• Tel: 786-540-3316 Fax: 786-540-3389
Nice to have
• unique look
Should not have
• doesn't need QR like our current card has.

```html
<!DOCTYPE html>
<html lang="en">
<head>
<meta charset="utf-8">
<title>Dalton &amp; Vesh Business Card</title>
<link href="https://fonts.googleapis.com/css2?family=Open+Sans:ital,wght@0,400;0,500;1,400&display=swap" rel="stylesheet">
<style>
  :root {
    --blue-deep: #0555a3;
    --blue-mid: #3277b5;
    --blue-panel: #3a7cbc;
    --blue-light: #85acd3;
    --white: #ffffff;
    --brand-ink: #2f3e9e;
  }
  * { margin: 0; padding: 0; box-sizing: border-box; }
  html, body { width: 1200px; height: 653px; overflow: hidden; background: var(--white); }
  body { font-family: "Open Sans", Verdana, sans-serif; }
  .card { position: relative; width: 1200px; height: 653px; background: var(--white); overflow: hidden; }
  .panel-shape { position: absolute; left: 0; top: 0; }
  .info { position: absolute; left: 0; top: 0; width: 785px; height: 653px; color: var(--white); }
  .doctors { position: absolute; left: 150px; top: 24px; font-size: 30px; font-weight: 500; line-height: 28px; letter-spacing: 0.3px; }
  .rule { position: absolute; left: 141px; width: 530px; height: 2px; background: var(--white); }
  .rule--top { top: 104px; }
  .rule--bottom { top: 182px; }
  .credential { position: absolute; left: 151px; top: 111px; font-size: 24px; font-style: italic; line-height: 32px; }
  .contact { position: absolute; left: 98px; display: flex; align-items: center; gap: 12px; }
  .contact svg { flex: none; }
  .contact p { font-size: 20px; line-height: 25px; letter-spacing: 0.2px; }
  .contact .indent { padding-left: 7px; }
  .brand { position: absolute; left: 830px; top: 220px; width: 350px; display: flex; flex-direction: column; align-items: center; gap: 22px; text-align: center; }
  .brand-dot { width: 60px; height: 60px; border-radius: 50%; background: var(--brand-ink); }
  .brand-name { font-size: 26px; font-weight: 500; line-height: 36px; color: var(--brand-ink); }
</style>
</head>
<body>
<main class="card">
  <svg class="panel-shape" width="785" height="653" viewBox="0 0 785 653" aria-hidden="true">
    <defs>
      <linearGradient id="panelFill" x1="0" y1="0" x2="1" y2="1">
        <stop offset="0" stop-color="#4a86c2"/>
        <stop offset="0.5" stop-color="#3a7cbc"/>
        <stop offset="1" stop-color="#3277b5"/>
      </linearGradient>
    </defs>
    <path d="M0 0 H785 V56 Q785 64 777 66 L758 70 Q746 73 746 86 V590 Q746 603 758 606 L777 610 Q785 612 785 620 V653 H0 Z" fill="url(#panelFill)"/>
  </svg>

  <section class="info">
    <h1 class="doctors">Gavin T. Dalton D.M.D.<br>Marla P. Vesh D.M.D.</h1>
    <div class="rule rule--top"></div>
    <p class="credential">Diplomate of the National Council of<br>Gum Surgery</p>
    <div class="rule rule--bottom"></div>

    <div class="contact" style="top:204px">
      <svg width="42" height="42" viewBox="0 0 42 42" aria-hidden="true"><circle cx="21" cy="21" r="19" fill="none" stroke="#fff" stroke-width="2"/><path d="M21 10a7 7 0 0 0-7 7c0 5.5 7 14 7 14s7-8.5 7-14a7 7 0 0 0-7-7zm0 10a3 3 0 1 1 0-6 3 3 0 0 1 0 6z" fill="none" stroke="#fff" stroke-width="2"/></svg>
      <p>462 N. Larkspur Avenue Suite 210B Plantation,<br><span class="indent">FL 33324</span></p>
    </div>
    <div class="contact" style="top:283px">
      <svg width="42" height="42" viewBox="0 0 42 42" aria-hidden="true"><circle cx="21" cy="21" r="19" fill="none" stroke="#fff" stroke-width="2"/><path d="M15 11l4 5-2 3c1.5 3 3.5 5 6 6.5l3-2 5 4-2 3.5c-7 0-15-8-16-16z" fill="none" stroke="#fff" stroke-width="2" stroke-linejoin="round"/></svg>
      <p>954-603-2281<br>Fax: 954-603-2895</p>
    </div>
    <div class="contact" style="top:361px">
      <svg width="42" height="42" viewBox="0 0 42 42" aria-hidden="true"><circle cx="21" cy="21" r="19" fill="none" stroke="#fff" stroke-width="2"/><path d="M21 10a7 7 0 0 0-7 7c0 5.5 7 14 7 14s7-8.5 7-14a7 7 0 0 0-7-7zm0 10a3 3 0 1 1 0-6 3 3 0 0 1 0 6z" fill="none" stroke="#fff" stroke-width="2"/></svg>
      <p>5174 Hollins Lane #C-3 Boca Raton,<br><span class="indent">FL 33434</span></p>
    </div>
    <div class="contact" style="top:440px">
      <svg width="42" height="42" viewBox="0 0 42 42" aria-hidden="true"><circle cx="21" cy="21" r="19" fill="none" stroke="#fff" stroke-width="2"/><path d="M15 11l4 5-2 3c1.5 3 3.5 5 6 6.5l3-2 5 4-2 3.5c-7 0-15-8-16-16z" fill="none" stroke="#fff" stroke-width="2" stroke-linejoin="round"/></svg>
      <p>561-327-6018<br>Fax: 561-327-6092</p>
    </div>
    <div class="contact" style="top:518px">
      <svg width="42" height="42" viewBox="0 0 42 42" aria-hidden="true"><circle cx="21" cy="21" r="19" fill="none" stroke="#fff" stroke-width="2"/><path d="M21 10a7 7 0 0 0-7 7c0 5.5 7 14 7 14s7-8.5 7-14a7 7 0 0 0-7-7zm0 10a3 3 0 1 1 0-6 3 3 0 0 1 0 6z" fill="none" stroke="#fff" stroke-width="2"/></svg>
      <p>381 Northwest 7th Street #412 Miami<br><span class="indent">FL 33131</span></p>
    </div>
    <div class="contact" style="top:596px">
      <svg width="42" height="42" viewBox="0 0 42 42" aria-hidden="true"><circle cx="21" cy="21" r="19" fill="none" stroke="#fff" stroke-width="2"/><path d="M15 11l4 5-2 3c1.5 3 3.5 5 6 6.5l3-2 5 4-2 3.5c-7 0-15-8-16-16z" fill="none" stroke="#fff" stroke-width="2" stroke-linejoin="round"/></svg>
      <p>786-540-3316<br>Fax: 786-540-3389</p>
    </div>
  </section>

  <aside class="brand">
    <div class="brand-dot" aria-hidden="true"></div>
    <p class="brand-name">Dalton &amp; Vesh Periodontics and Implant Solutions</p>
  </aside>
</main>
</body>
</html>
```